Ductless Mini Split Business Website

Tall Fern Services is looking to design an eye catching educational website about installing Ductless mini splits.

Similar to this company.
https://www.kelvarocomfort.com/

```html
<!DOCTYPE html>
<html lang="en">
<head>
<meta charset="utf-8">
<title>Tall Fern Services – Ductless Experts</title>
<link rel="stylesheet" href="https://fonts.googleapis.com/css2?family=Raleway:wght@400;500;600;700&display=swap">
<style>
  :root{
    --yellow:#ffe200;
    --ink:#1b1b1b;
    --dark:#1e1e1e;
    --panel:#f1f1f1;
    --body:#555555;
    --white:#ffffff;
    --footer-line:#eeeeee;
  }
  *{margin:0;padding:0;box-sizing:border-box}
  html,body{width:1200px;height:3244px;overflow:hidden;background:var(--white)}
  body{position:relative;font-family:"Raleway",sans-serif;color:var(--ink)}
  .abs{position:absolute}

  /* header */
  .site-header{left:0;top:0;width:1200px;height:102px;background:var(--white)}
  .brand{left:368px;top:34px;display:flex;align-items:center;gap:10px}
  .brand-mark{width:34px;height:34px;border-radius:50%;background:var(--yellow)}
  .brand-name{font-size:22px;font-weight:700;color:var(--ink);letter-spacing:.2px}
  .brand-tag{font-size:21px;font-weight:700;color:#e8c800;letter-spacing:.5px;margin-left:8px}
  .consult-btn{left:963px;top:38px;width:149px;height:37px;border:2px solid var(--ink);font-size:14px;display:flex;align-items:center;justify-content:center;color:var(--ink)}

  .main-nav{left:0;top:102px;width:1200px;height:52px;background:var(--dark)}
  .nav-item{top:0;height:52px;line-height:52px;color:var(--white);font-size:14px;font-weight:500;transform:translateX(-50%);white-space:nowrap}

  /* hero */
  .hero{left:0;top:154px;width:1200px;height:576px;background:linear-gradient(180deg,#4a505c 0%,#3e434d 60%,#2f3136 100%)}
  .hero-title{left:0;top:370px;width:1200px;text-align:center;color:var(--white);font-size:41px;font-weight:500;line-height:47px}

  /* intro */
  .intro-heading{left:89px;top:828px;font-size:28px;font-weight:700;color:var(--ink)}
  .intro-copy{left:481px;top:802px;width:640px;font-size:16.5px;line-height:28px;color:var(--body)}

  /* services */
  .services{left:0;top:980px;width:1200px;height:1148px;background:var(--panel)}
  .service-card{width:407px;height:386px}
  .service-photo{position:absolute;inset:0}
  .service-label{position:absolute;left:0;bottom:0;height:70px;background:var(--yellow);display:flex;align-items:center;padding-left:22px;font-size:15px;font-weight:600;color:var(--ink);gap:22px}
  .chev{width:10px;height:14px}

  /* testimonials */
  .testi-heading{left:0;top:2190px;width:1200px;text-align:center;font-size:28px;font-weight:500}
  .slider-arrow{top:2272px;height:361px;background:var(--yellow);display:flex;align-items:center;justify-content:center}
  .testi-panel{left:159px;top:2272px;width:888px;height:361px;background:var(--panel);text-align:center}
  .client-name{position:absolute;left:0;width:888px;top:70px;font-size:24px;font-weight:700;color:#1d4f8c}
  .quote{position:absolute;left:134px;width:620px;top:152px;font-size:15px;line-height:24.5px;color:var(--body)}
  .quote-author{position:absolute;left:0;width:888px;top:278px;font-size:15px;color:var(--body)}

  /* footer */
  .site-footer{left:0;top:2725px;width:1200px;height:440px;background:var(--dark)}
  .cta-text{left:150px;top:2796px;width:360px;font-size:22px;line-height:37px;color:var(--yellow)}
  .call-title{left:640px;top:2795px;font-size:29px;font-weight:700;color:var(--yellow)}
  .contact-line{left:640px;font-size:27px;color:var(--white);display:flex}
  .contact-line span:first-child{width:63px}
  .to-top{left:1015px;top:3080px;width:96px;height:85px;background:var(--footer-line);display:flex;align-items:center;justify-content:center}
  .copyright-bar{left:0;top:3165px;width:1200px;height:79px;background:var(--footer-line);text-align:center;line-height:79px;font-size:12px;color:var(--ink)}
</style>
</head>
<body>

<header class="site-header abs">
  <div class="brand abs">
    <span class="brand-mark"></span>
    <span class="brand-name">Tall Fern Services</span>
    <span class="brand-tag">DUCTLESS EXPERTS</span>
  </div>
  <a class="consult-btn abs">Consult us today</a>
</header>

<nav class="main-nav abs">
  <span class="nav-item abs" style="left:227px">Home</span>
  <span class="nav-item abs" style="left:351px">About Us</span>
  <span class="nav-item abs" style="left:512px">Ductless Solutions</span>
  <span class="nav-item abs" style="left:677px">Products</span>
  <span class="nav-item abs" style="left:795px">FAQ</span>
  <span class="nav-item abs" style="left:931px">Contact Us</span>
</nav>

<section class="hero abs" role="img" aria-label="Dim grey room interior with an armchair, wall shelf, clock and pendant lamps"></section>
<h1 class="hero-title abs">Technologies to improve<br>efficiency at work and home.</h1>

<h2 class="intro-heading abs">The Experts In Ductless</h2>
<p class="intro-copy abs">We are experts in ductless heating and cooling. We provide reliable services and you can count on us for solutions that closely meet your requirements. The sophisticated ductless ACs and heat pumps we offer can be configured to the precise settings your home needs.</p>

<section class="services abs"></section>

<div class="service-card abs" style="left:145px;top:1126px">
  <div class="service-photo" role="img" aria-label="Contractor in hard hat shaking hands with a client" style="background:linear-gradient(160deg,#8a8f92 0%,#c9c3b4 50%,#e9e6dc 100%)"></div>
  <div class="service-label" style="width:291px">Efficiency Ally Contractor
    <svg class="chev" viewBox="0 0 10 14"><path d="M2 1l6 6-6 6" fill="none" stroke="#1b1b1b" stroke-width="2"/></svg></div>
</div>

<div class="service-card abs" style="left:657px;top:1052px">
  <div class="service-photo" role="img" aria-label="Smiling financial advisor in an office with binders" style="background:linear-gradient(90deg,#e8eaec 0%,#c8ccd2 50%,#f3f3f3 100%)"></div>
  <div class="service-label" style="width:286px">Ductless Financing Options
    <svg class="chev" viewBox="0 0 10 14"><path d="M2 1l6 6-6 6" fill="none" stroke="#1b1b1b" stroke-width="2"/></svg></div>
</div>

<div class="service-card abs" style="left:145px;top:1643px">
  <div class="service-photo" role="img" aria-label="Wall-mounted ductless air conditioner unit in a bright room" style="background:linear-gradient(160deg,#d8e2ec 0%,#eef2f6 55%,#c5cfd8 100%)"></div>
  <div class="service-label" style="width:244px">Ductless Maintenance
    <svg class="chev" viewBox="0 0 10 14"><path d="M2 1l6 6-6 6" fill="none" stroke="#1b1b1b" stroke-width="2"/></svg></div>
</div>

<div class="service-card abs" style="left:657px;top:1549px">
  <div class="service-photo" role="img" aria-label="Technician adjusting a wall thermostat control" style="background:linear-gradient(120deg,#55585d 0%,#bdbab4 45%,#e4e1dc 100%)"></div>
  <div class="service-label" style="width:285px">Ductles Repairs &amp; Warranty
    <svg class="chev" viewBox="0 0 10 14"><path d="M2 1l6 6-6 6" fill="none" stroke="#1b1b1b" stroke-width="2"/></svg></div>
</div>

<h2 class="testi-heading abs">Testimonials</h2>

<div class="slider-arrow abs" style="left:0;width:139px">
  <svg width="16" height="26" viewBox="0 0 16 26"><path d="M13 2L3 13l10 11" fill="none" stroke="#1b1b1b" stroke-width="2.5"/></svg>
</div>
<div class="testi-panel abs">
  <div class="client-name">Norvane Labs</div>
  <p class="quote">“I have worked with Tall Fern Services over the years because of their reliable solutions. The work is always high quality, on schedule, fairly priced and done by a team you can trust. I recommend Tall Fern Services to anyone looking for professional ductless solutions.”</p>
  <div class="quote-author">Martin Hale, Norvane Labs</div>
</div>
<div class="slider-arrow abs" style="left:1064px;width:136px">
  <svg width="16" height="26" viewBox="0 0 16 26"><path d="M3 2l10 11L3 24" fill="none" stroke="#1b1b1b" stroke-width="2.5"/></svg>
</div>

<footer class="site-footer abs"></footer>
<p class="cta-text abs">Contact us for a free quote and start building something great with us today.</p>
<div class="call-title abs">Call now</div>
<div class="contact-line abs" style="top:2855px"><span>M:</span><span>+011 5550 0142</span></div>
<div class="contact-line abs" style="top:2898px"><span>E:</span><span>info@tallfernservices.com</span></div>
<div class="to-top abs">
  <svg width="28" height="16" viewBox="0 0 28 16"><path d="M14 1L27 15H1z" fill="#1b1b1b"/></svg>
</div>
<div class="copyright-bar abs">Copyright © 2020 Tall Fern Services. All rights reserved.</div>

</body>
</html>
```